Memento Mori Calendar

I’m looking for a graphic designer to create a Memento Mori–style life calendar that captures the essence of OLVENTRA — minimal, timeless, and deeply philosophical.

The design should be black and white only, with a refined, clean aesthetic and a sense of stillness and precision.
It should feel modern yet eternal, reflecting the themes of time, mortality, and presence.

Deliverables (Print-Ready Files):

24 x 30 in

24 x 32 in

24 x 36 in

A1 (594 x 841 mm)

All formats should be high-resolution and ready for professional printing (300 DPI, CMYK).

Design Requirements:

The calendar layout should follow the Memento Mori life calendar concept (weeks of life represented as small squares or circles).

The overall tone: minimal, meditative, monochrome.

Include the brand name: OLVENTRA (in an elegant, understated placement).

Add the following quote at the bottom or in a subtle position:

“Life can only be understood backwards; but it must be lived forwards.”
— Henrik Vastmoe

Target Market(s)

The OLVENTRA audience consists of urban, creative individuals aged 25 to 45, belonging to a middle to upper-middle income class. They lead conscious, quietly ambitious lives, seeking balance between inner depth and modern design. Their values center on awareness, presence, authenticity, and emotional depth, reflected in their preference for a monochrome, minimal, and timeless aesthetic. They tend to be introverted, reflective, and spiritually curious, drawn to brands that embody meaning and restraint rather than excess. Their cultural and stylistic affinities include Pyrel, Tulve, Ni Ostra, The Quiet Bench Guild, Durvanne, and Ombrix — labels that share OLVENTRAs devotion to simplicity, substance, and subtle ritual.

Font styles to use
Serif
Sans Serif

Colors

Designer to choose only greyscale colors for use in the design.

Requirements
Must have
• The calendar layout should follow the Memento Mori life calendar concept (weeks of life represented as small squares or circles). The overall tone: minimal, meditative, monochrome. Include the brand name: qrnvalto (in an elegant, understated placement). Add the following quote at the bottom or in a subtle position: “Life can only be understood backwards; but it must be lived forwards.” — Henrik Vastmoe

```html
<!DOCTYPE html>
<html lang="en">
<head>
<meta charset="utf-8">
<title>Memento Mori — OLVENTRA Life Calendar</title>
<link rel="stylesheet" href="https://fonts.googleapis.com/css2?family=Poppins:wght@400;500;600;700&display=swap">
<style>
  :root {
    --ink: #000000;
    --paper: #ffffff;
    --rule: #1a1a1a;
  }
  html, body {
    margin: 0;
    padding: 0;
    width: 940px;
    height: 1200px;
    overflow: hidden;
    background: var(--paper);
  }
  .poster {
    position: relative;
    width: 940px;
    height: 1200px;
    background: var(--paper);
    color: var(--ink);
    font-family: "Poppins", sans-serif;
  }
  .poster__title {
    position: absolute;
    right: 98px;
    top: 34px;
    margin: 0;
    font-size: 62px;
    font-weight: 700;
    letter-spacing: -0.5px;
    line-height: 1;
  }
  .life-grid {
    position: absolute;
    left: 0;
    top: 0;
  }
  .axis-title {
    font-family: "Poppins", sans-serif;
    font-weight: 700;
    font-size: 12px;
    fill: var(--ink);
  }
  .axis-number {
    font-family: "Poppins", sans-serif;
    font-weight: 400;
    font-size: 8.5px;
    fill: var(--ink);
  }
  .brand-name {
    position: absolute;
    left: 90px;
    top: 1130px;
    margin: 0;
    font-size: 22px;
    font-weight: 500;
    letter-spacing: 1px;
    line-height: 32px;
  }
  .closing-quote {
    position: absolute;
    right: 89px;
    top: 1130px;
    margin: 0;
    text-align: right;
  }
  .closing-quote__text {
    margin: 0;
    font-size: 15px;
    font-weight: 400;
    line-height: 18px;
  }
  .closing-quote__author {
    display: block;
    font-size: 10.5px;
    font-weight: 400;
    font-style: normal;
    line-height: 14px;
  }
</style>
</head>
<body>
<main class="poster">
  <h1 class="poster__title">MEMENTO MORI</h1>

  <svg class="life-grid" width="940" height="1200" viewBox="0 0 940 1200" aria-label="Life calendar: 80 years by 52 weeks">
    <defs>
      <pattern id="week-cell" patternUnits="userSpaceOnUse" width="14.07" height="10.6">
        <rect x="0.5" y="0.5" width="7.6" height="7.6" fill="none" stroke="#000" stroke-width="0.9"/>
      </pattern>
      <pattern id="decade-dot-left" patternUnits="userSpaceOnUse" x="126.1" y="141" width="70.35" height="120.6">
        <circle cx="35.17" cy="113" r="1.6" fill="#000"/>
      </pattern>
      <pattern id="decade-dot-right" patternUnits="userSpaceOnUse" x="490" y="141" width="70.35" height="120.6">
        <circle cx="35.17" cy="113" r="1.6" fill="#000"/>
      </pattern>
    </defs>

    <!-- week axis -->
    <text class="axis-title" x="101" y="113">WEEK</text>
    <line x1="101" y1="117.5" x2="839" y2="117.5" stroke="var(--rule)" stroke-width="0.8"/>
    <g class="axis-number" text-anchor="middle">
      <text x="161.3" y="132">5</text>
      <text x="231.6" y="132">10</text>
      <text x="302" y="132">15</text>
      <text x="372.3" y="132">20</text>
      <text x="442.7" y="132">25</text>
      <text x="525.2" y="132">30</text>
      <text x="595.6" y="132">35</text>
      <text x="665.9" y="132">40</text>
      <text x="736.3" y="132">45</text>
      <text x="806.6" y="132">50</text>
    </g>

    <!-- decade blocks -->
    <g class="decade-blocks" fill="url(#week-cell)">
      <g transform="translate(101 141)"><rect width="366" height="106"/></g>
      <g transform="translate(479 141)"><rect width="366" height="106"/></g>
      <g transform="translate(101 261.6)"><rect width="366" height="106"/></g>
      <g transform="translate(479 261.6)"><rect width="366" height="106"/></g>
      <g transform="translate(101 382.2)"><rect width="366" height="106"/></g>
      <g transform="translate(479 382.2)"><rect width="366" height="106"/></g>
      <g transform="translate(101 502.8)"><rect width="366" height="106"/></g>
      <g transform="translate(479 502.8)"><rect width="366" height="106"/></g>
      <g transform="translate(101 623.4)"><rect width="366" height="106"/></g>
      <g transform="translate(479 623.4)"><rect width="366" height="106"/></g>
      <g transform="translate(101 744)"><rect width="366" height="106"/></g>
      <g transform="translate(479 744)"><rect width="366" height="106"/></g>
      <g transform="translate(101 864.6)"><rect width="366" height="106"/></g>
      <g transform="translate(479 864.6)"><rect width="366" height="106"/></g>
      <g transform="translate(101 985.2)"><rect width="366" height="106"/></g>
      <g transform="translate(479 985.2)"><rect width="366" height="106"/></g>
    </g>

    <!-- markers between decades -->
    <rect x="126.1" y="141" width="351.75" height="844.2" fill="url(#decade-dot-left)"/>
    <rect x="490" y="141" width="351.75" height="844.2" fill="url(#decade-dot-right)"/>

    <!-- mid-decade side markers -->
    <g class="side-markers" fill="#000">
      <circle cx="89" cy="188" r="2"/><circle cx="851" cy="188" r="2"/>
      <circle cx="89" cy="308.6" r="2"/><circle cx="851" cy="308.6" r="2"/>
      <circle cx="89" cy="429.2" r="2"/><circle cx="851" cy="429.2" r="2"/>
      <circle cx="89" cy="549.8" r="2"/><circle cx="851" cy="549.8" r="2"/>
      <circle cx="89" cy="670.4" r="2"/><circle cx="851" cy="670.4" r="2"/>
      <circle cx="89" cy="791" r="2"/><circle cx="851" cy="791" r="2"/>
      <circle cx="89" cy="911.6" r="2"/><circle cx="851" cy="911.6" r="2"/>
      <circle cx="89" cy="1032.2" r="2"/><circle cx="851" cy="1032.2" r="2"/>
    </g>

    <!-- year axis -->
    <g class="axis-number" font-size="10" text-anchor="middle">
      <text transform="translate(850 240) rotate(90)">10</text>
      <text transform="translate(850 360.6) rotate(90)">20</text>
      <text transform="translate(850 481.2) rotate(90)">30</text>
      <text transform="translate(850 601.8) rotate(90)">40</text>
      <text transform="translate(850 722.4) rotate(90)">50</text>
      <text transform="translate(850 843) rotate(90)">60</text>
      <text transform="translate(850 963.6) rotate(90)">70</text>
      <text transform="translate(850 1084.2) rotate(90)">80</text>
    </g>
    <line x1="867.5" y1="143" x2="867.5" y2="1089" stroke="var(--rule)" stroke-width="0.8"/>
    <text class="axis-title" text-anchor="middle" transform="translate(877 600) rotate(90)">YEAR</text>
  </svg>

  <p class="brand-name">OLVENTRA</p>

  <blockquote class="closing-quote">
    <p class="closing-quote__text">“Life can only be understood backwards; but it must be lived forwards.”</p>
    <cite class="closing-quote__author">Henrik Vastmoe</cite>
  </blockquote>
</main>
</body>
</html>
```